Need Business Card for our Indian Grocery Store

Industry/Entity Type

Grocery Store

Contact Information for Business Card

Manoj Baweja
Director

Store Locations:

Elmbrook
482 Elm Parade
P: 03 9172 5843

Carlow Heights
613 Carlow Road
P: 03 9238 6014

email: kvtmarts@mailnest.example

Requirements
Must have
• Our logo Colours

```html
<!DOCTYPE html>
<html lang="en">
<head>
<meta charset="utf-8">
<title>KVT Business Card</title>
<link href="https://fonts.googleapis.com/css2?family=Roboto:wght@400;500;700&display=swap" rel="stylesheet">
<style>
  :root {
    --stage: #2b2b2b;
    --brand-red: #e10f06;
    --back-red: #e31f29;
    --paper: #f2f2f2;
    --white: #ffffff;
  }
  html, body { margin: 0; padding: 0; overflow: hidden; }
  body {
    width: 1200px; height: 960px;
    background: var(--stage);
    position: relative;
    font-family: 'Roboto', Arial, sans-serif;
  }
  .card {
    position: absolute;
    width: 598px; height: 342px;
    border-radius: 16px;
    overflow: hidden;
    box-shadow: 0 6px 10px rgba(0,0,0,.5);
  }
  .card-front { left: 322px; top: 108px; background: var(--paper); }
  .card-back { left: 320px; top: 493px; width: 600px; background: var(--back-red); }
  .front-shape { position: absolute; inset: 0; }
  .brand-lockup {
    position: absolute; left: 46px; top: 52px; width: 228px;
    text-align: center; color: var(--brand-red); font-weight: 700;
  }
  .brand-name { font-size: 72px; line-height: 1; letter-spacing: 3px; }
  .brand-sub { font-size: 15px; letter-spacing: 1px; margin-top: 14px; }
  .contact {
    position: absolute; right: 26px; top: 117px;
    text-align: right; color: var(--white);
    font-size: 14px; line-height: 18px;
  }
  .contact-name { font-size: 20px; font-weight: 700; line-height: 22px; }
  .contact-role { font-size: 15px; font-weight: 500; line-height: 18px; margin-bottom: 10px; }
  .store { margin-bottom: 6px; }
  .store b { font-weight: 700; }
  .web-line { display: flex; justify-content: flex-end; align-items: center; gap: 7px; }
  .web-line svg { width: 13px; height: 13px; }
  .contact-web { margin-top: 10px; }
  .back-brand {
    position: absolute; inset: 0;
    display: flex; align-items: center; justify-content: center;
    color: var(--white); font-weight: 700; font-size: 84px; letter-spacing: 4px;
  }
</style>
</head>
<body>
  <section class="card card-front">
    <svg class="front-shape" viewBox="0 0 598 342" aria-hidden="true">
      <path d="M372,0 C412,40 416,140 356,214 C300,282 258,296 258,342" fill="none" stroke="#e10f06" stroke-width="2"/>
      <path d="M380,0 C420,42 424,144 364,218 C308,286 266,300 266,342 L598,342 L598,0 Z" fill="#e10f06"/>
    </svg>
    <div class="brand-lockup">
      <div class="brand-name">KVT</div>
      <div class="brand-sub">GROCERIES &amp; SPICES</div>
    </div>
    <div class="contact">
      <div class="contact-name">MANOJ BAWEJA</div>
      <div class="contact-role">DIRECTOR</div>
      <div class="store">Elmbrook<br>482 Elm Parade<br><b>P</b> 03 9172 5843</div>
      <div class="store">Carlow Heights<br>613 Carlow Road<br><b>P</b> 03 9238 6014</div>
      <div class="contact-web">
        <div class="web-line">kvtmarts@mailnest.example
          <svg viewBox="0 0 14 14"><rect x="1" y="3" width="12" height="8" fill="#fff"/><path d="M1,3 L7,8 L13,3" fill="none" stroke="#e10f06" stroke-width="1.2"/></svg>
        </div>
        <div class="web-line">www.kvtmarts.example
          <svg viewBox="0 0 14 14"><circle cx="7" cy="7" r="6" fill="#fff"/><path d="M1,7 H13 M7,1 C4,4 4,10 7,13 M7,1 C10,4 10,10 7,13" fill="none" stroke="#e10f06" stroke-width="1"/></svg>
        </div>
      </div>
    </div>
  </section>
  <section class="card card-back">
    <div class="back-brand">KVT</div>
  </section>
</body>
</html>
```